Website Update for Global Company - Solar Technology - Brisqell

We recently released our first version of our website kelvaris.com. However despite a longer process of developing the page, it is still missing the elements of a brilliant website. (Currently it looks dead and boring) We are having problems integrating our logo and want to create a more catching site. The task involves an updated and without changing most of main elements in the existing page. (Unless you can do it even better) The blue color needs to be kept but can be changed within the blue-spectrum. The logo text (KELVARIS) must be better integrated in the site, however the main logo could be used in elements like we have tried with the background. The surface of the logo could be changed to 3D or metallic, or any other theme that would make the site more complete.
It would be good if some elements of the site could be used on business cards and invoices to keep the company identity.
Kelvaris is a new development company specialized in green energy and sustainable development. We do design, engineering, manufacturing, sourcing and other processes related to product development – both as consultants and for own products.
Keep the look of the site as professional as possible, and with a cooperate-looking style.

Link to existing page: www.kelvaris.com

Brief Update : After reviewing the designs we would like all new and current designers to make more bold designs that stands out from the rest. We do not like the standard layout that looks like any other cooperate homepage. We want a very unique and very lively page - with faded images and effects when hoovering like seen on our existing page. Try make all elements blend together, and use faded background images instead of just white color - or something else.

Make the site unique !

Industry/Entity Type

Solar Energy

Contact Information for Business Card

Owner/Founder/CEO : Frederik Lysgaard Holm
Company name: Kelvaris ApS
Email: frederik.lysgaard@kelvaris.dk
Phone: +45 71 83 96 54
Slogan Sustainable Development
Address: Havnestien 18, 2
DK-5820 Svendborg, Denmark

Number of Pages Required

3 page

Font styles to use
Serif
Sans Serif

Colors
0555a3
85acd3
cedeed
3176b5
cee9f5
85cae6
0293ce
86cfc6
33b8a4

```html
<!DOCTYPE html>
<html lang="en">
<head>
<meta charset="utf-8">
<title>Kelvaris — Sustainable Solutions</title>
<link href="https://fonts.googleapis.com/css2?family=Open+Sans:wght@400;600;700&family=Raleway:wght@500;700;800&display=swap" rel="stylesheet">
<style>
:root{
  --blue-deep:#0555a3;
  --blue-mid:#3176b5;
  --blue-bright:#0293ce;
  --blue-soft:#85acd3;
  --blue-pale:#cedeed;
  --blue-ice:#cee9f5;
  --sky:#85cae6;
  --ink:#2b2f36;
  --grey:#7c8590;
  --bar:#26292e;
  --white:#ffffff;
}
*{box-sizing:border-box;margin:0;padding:0}
html,body{width:1200px;height:2632px;overflow:hidden}
body{font-family:"Open Sans",Arial,sans-serif;color:var(--ink);background:var(--white);position:relative}
.grid-bg{background-color:#dbe9f3;background-image:linear-gradient(rgba(255,255,255,.45) 1px,transparent 1px),linear-gradient(90deg,rgba(255,255,255,.45) 1px,transparent 1px);background-size:24px 24px}

/* top bar */
.topbar{height:32px;background:var(--bar);color:#c9cdd3;font-size:11px;display:flex;align-items:center;padding:0 160px;gap:22px}
.topbar .search{margin-left:auto}
/* header */
.header{height:76px;display:flex;align-items:center;padding:0 160px;background:var(--white)}
.brand{display:flex;align-items:center;gap:12px}
.brand-mark{width:34px;height:34px;background:var(--blue-deep)}
.brand-name{font-family:"Raleway",sans-serif;font-weight:800;font-size:30px;letter-spacing:2px;color:var(--blue-deep)}
.brand-sub{font-size:10px;letter-spacing:3px;color:var(--blue-mid);margin-top:-4px}
.nav{margin-left:auto;display:flex;gap:22px;font-size:11px;font-weight:700;color:#555}
.nav a{color:inherit;text-decoration:none;padding-bottom:6px}
.nav a.active{color:var(--blue-deep);border-bottom:2px solid var(--blue-deep)}

/* hero */
.hero{position:relative;height:552px;background:
  radial-gradient(ellipse 600px 180px at 75% 8%,rgba(255,255,255,.95),transparent 70%),
  linear-gradient(168deg,#f2f7fb 0%,#dbe9f4 26%,#b9d2e8 36%,#6f93bf 42%,#34598f 55%,#1d3b6b 72%,#2b4f82 86%,#163058 100%)}
.hero::after{content:"";position:absolute;inset:0;background:linear-gradient(90deg,rgba(10,30,60,.25) 0%,transparent 35%,transparent 70%,rgba(10,30,60,.2) 100%)}
.hero-copy{position:absolute;right:220px;top:120px;text-align:right;color:var(--white);z-index:1}
.hero-copy .welcome{font-family:"Raleway",sans-serif;font-size:30px;font-weight:700;text-shadow:0 1px 3px rgba(0,0,0,.3)}
.hero-copy .title{font-family:"Raleway",sans-serif;font-size:30px;margin-top:4px;color:#1b2e4a}
.hero-copy .title b{font-weight:800;letter-spacing:2px}
.hero-copy .tag{display:inline-flex;align-items:center;gap:10px;margin-top:6px;font-size:15px;font-weight:700;color:#1b2e4a}
.hero-copy .tag i{display:inline-block;width:30px;height:12px;background:var(--blue-bright)}
.arrow{position:absolute;top:230px;z-index:1}

/* section headings */
.sec-title{font-family:"Raleway",sans-serif;font-weight:800;font-size:22px;letter-spacing:2px;color:var(--blue-deep);text-align:center}
.sec-sub{font-size:12px;color:var(--grey);text-align:center;margin-top:10px}
.divider{display:flex;align-items:center;justify-content:center;margin:12px auto 0}
.divider span{width:60px;height:2px;background:var(--blue-soft)}
.divider i{width:10px;height:10px;border:2px solid var(--blue-mid);border-radius:50%;background:var(--white)}

/* why */
.why{height:392px;padding-top:60px}
.features{display:flex;justify-content:center;gap:96px;margin-top:40px}
.feature{width:140px;text-align:center}
.feature .icon{width:92px;height:76px;margin:0 auto;background:var(--white);border:2px solid var(--blue-pale);display:flex;align-items:center;justify-content:center}
.feature.active .icon{border-color:var(--blue-bright)}
.feature h3{font-size:11px;font-weight:700;color:var(--blue-deep);margin-top:12px;letter-spacing:1px;white-space:nowrap}
.feature p{font-size:9px;color:var(--grey);margin-top:6px;line-height:1.4}

/* featured + news */
.split{display:flex;height:500px;margin-top:8px}
.featured{width:660px;position:relative;background:
  radial-gradient(ellipse 260px 200px at 30% 30%,rgba(255,255,255,.9),transparent 70%),
  radial-gradient(ellipse 300px 160px at 75% 85%,rgba(120,140,165,.55),transparent 70%),
  linear-gradient(135deg,#f1f4f7 0%,#d9e2ea 40%,#b6c4d2 70%,#8597ab 100%)}
.featured-label{position:absolute;left:250px;top:210px;width:280px;height:56px;background:rgba(120,160,200,.45);border:1px solid var(--white);display:flex;align-items:center;justify-content:center;font-family:"Raleway",sans-serif;font-weight:700;font-size:18px;color:var(--white);letter-spacing:1px;text-shadow:0 1px 2px rgba(0,0,0,.3)}
.news{flex:1;border-left:4px solid var(--blue-mid);padding:36px 40px 0 40px;position:relative}
.news .sec-title{font-size:20px}
.news-list{margin-top:30px;display:flex;flex-direction:column;gap:14px;padding-left:20px}
.news-item{display:flex;gap:18px;align-items:flex-start}
.date{width:44px;height:56px;background:var(--blue-mid);color:var(--white);text-align:center;font-weight:700;font-size:12px;line-height:1.3;padding-top:9px;flex:none}
.date.light{background:var(--blue-soft)}
.news-item p{font-size:10px;color:var(--grey);line-height:1.5;width:290px;padding-top:4px}
.scroll{position:absolute;right:42px;top:150px;width:6px;height:300px;background:var(--blue-pale)}
.scroll i{display:block;width:6px;height:70px;background:var(--blue-bright)}

/* works */
.works{height:828px;padding-top:60px}
.filters{display:flex;gap:22px;margin:36px 0 0 210px;font-size:12px;color:#444;align-items:center}
.filters .on{background:var(--blue-bright);color:var(--white);padding:3px 8px}
.tiles{display:grid;grid-template-columns:repeat(3,293px);grid-auto-rows:242px;gap:3px;margin:18px 0 0 160px}
.tile{position:relative;display:flex;align-items:center;justify-content:center}
.tile span{font-family:"Raleway",sans-serif;font-weight:700;letter-spacing:2px;color:var(--white);font-size:12px}
.more{display:block;width:84px;margin:22px auto 0;background:var(--white);border:1px solid var(--blue-soft);color:var(--blue-mid);font-size:10px;text-align:center;padding:5px 0}

/* footer */
.footer{height:212px;border-top:6px solid var(--blue-mid);display:flex;padding:16px 160px 0;gap:70px}
.footer h4{font-size:15px;font-weight:700;color:var(--blue-deep);margin-bottom:10px}
.about{width:230px}
.about p{font-size:10px;color:var(--grey);line-height:1.5}
.about .brand{margin-top:12px}
.about .brand-name{font-size:26px}
.tags{display:grid;grid-template-columns:repeat(3,auto);gap:6px;width:240px}
.tags span{font-size:9px;color:var(--grey);border:1px solid var(--blue-soft);background:var(--white);padding:3px 6px;text-align:center}
.tags span.on{background:var(--blue-bright);color:var(--white);border-color:var(--blue-bright)}
.links{display:grid;grid-template-columns:150px 150px;gap:9px 0;font-size:10px;color:var(--grey)}
.links li{list-style:none;display:flex;align-items:center;gap:8px}
.links li::before{content:"";width:8px;height:8px;background:var(--blue-mid)}
.copyright{position:absolute;left:0;bottom:0;width:1200px;height:32px;background:var(--blue-deep);color:var(--blue-ice);font-size:10px;display:flex;align-items:center;justify-content:center}
</style>
</head>
<body>

<div class="topbar">
  <span>☏ +45 71 83 96 54</span>
  <span>✉ support@kelvaris.com</span>
  <svg class="search" width="12" height="12" viewBox="0 0 12 12"><circle cx="5" cy="5" r="3.6" fill="none" stroke="#c9cdd3" stroke-width="1.5"/><line x1="7.7" y1="7.7" x2="11" y2="11" stroke="#c9cdd3" stroke-width="1.5"/></svg>
</div>

<header class="header">
  <div class="brand">
    <div class="brand-mark"></div>
    <div>
      <div class="brand-name">KELVARIS</div>
      <div class="brand-sub">SUSTAINABLE SOLUTIONS</div>
    </div>
  </div>
  <nav class="nav">
    <a class="active" href="#">HOME</a><a href="#">WORK</a><a href="#">EXPERTISE</a><a href="#">APPROACH</a><a href="#">CLIENTS</a><a href="#">ABOUT</a><a href="#">CONTACT</a>
  </nav>
</header>

<section class="hero" role="img" aria-label="Rows of solar panels under a bright pale sky">
  <svg class="arrow" style="left:160px" width="34" height="40" viewBox="0 0 34 40"><polygon points="30,3 4,20 30,37" fill="none" stroke="#fff" stroke-width="3"/></svg>
  <svg class="arrow" style="left:996px" width="34" height="40" viewBox="0 0 34 40"><polygon points="4,3 30,20 4,37" fill="none" stroke="#fff" stroke-width="3"/></svg>
  <div class="hero-copy">
    <div class="welcome">Welcome to our</div>
    <div class="title"><b>KELVARIS</b> Sustainable Solutions</div>
    <div class="tag">We are a team of professionals <i></i></div>
  </div>
</section>

<section class="why grid-bg">
  <h2 class="sec-title">WHY WE ARE DIFFERENT</h2>
  <p class="sec-sub">We provide complete services throughout the product development process</p>
  <div class="divider"><span></span><i></i><span></span></div>
  <div class="features">
    <div class="feature active">
      <div class="icon"><svg width="34" height="34" viewBox="0 0 34 34"><line x1="6" y1="28" x2="24" y2="10" stroke="#0293ce" stroke-width="4"/><path d="M24 4l2 4 4 2-4 2-2 4-2-4-4-2 4-2z" fill="#0293ce"/></svg></div>
      <h3>CREATIVE DESIGN</h3>
      <p>Ideas shaped into clear concepts with form, function and purpose.</p>
    </div>
    <div class="feature">
      <div class="icon"><svg width="34" height="34" viewBox="0 0 34 34"><circle cx="17" cy="17" r="9" fill="none" stroke="#0293ce" stroke-width="4" stroke-dasharray="5 2.5"/><circle cx="17" cy="17" r="4" fill="#0293ce"/></svg></div>
      <h3>ENGINEERING</h3>
      <p>Robust technical solutions tested for real world performance.</p>
    </div>
    <div class="feature">
      <div class="icon"><svg width="34" height="34" viewBox="0 0 34 34"><path d="M4 20a13 13 0 0 1 26 0z" fill="#0293ce"/><rect x="3" y="22" width="28" height="4" fill="#0293ce"/></svg></div>
      <h3>SOURCING</h3>
      <p>Reliable partners and materials found across global markets.</p>
    </div>
    <div class="feature">
      <div class="icon"><svg width="34" height="34" viewBox="0 0 34 34"><path d="M3 30V16l8 5v-5l8 5v-5l8 5V6h4v24z" fill="#0293ce"/></svg></div>
      <h3>MANUFACTURING</h3>
      <p>Efficient production set up with quality control at every step.</p>
    </div>
  </div>
</section>

<section class="split">
  <div class="featured" role="img" aria-label="Business person reviewing charts on a tablet at a desk">
    <div class="featured-label">FEATURED INNOVATION</div>
  </div>
  <div class="news grid-bg">
    <h2 class="sec-title">LATEST NEWS</h2>
    <p class="sec-sub">Our new and latest news of our company</p>
    <div class="divider"><span></span><i></i><span></span></div>
    <div class="news-list">
      <div class="news-item"><div class="date">08<br>AUG</div><p>New solar module line enters testing phase with partners in northern Europe this month.</p></div>
      <div class="news-item"><div class="date light">08<br>AUG</div><p>Our team presents sustainable design methods at the regional energy conference.</p></div>
      <div class="news-item"><div class="date">08<br>AUG</div><p>Engineering office expands with two new specialists in product development.</p></div>
      <div class="news-item"><div class="date light">08<br>AUG</div><p>Consulting project completed for efficient storage of locally produced energy.</p></div>
    </div>
    <div class="scroll"><i></i></div>
  </div>
</section>

<section class="works grid-bg">
  <h2 class="sec-title">OUR WORKS</h2>
  <p class="sec-sub">Kelvaris is made up of Kelvaris' Special Solutions</p>
  <div class="divider"><span></span><i></i><span></span></div>
  <div class="filters">
    <svg width="12" height="12" viewBox="0 0 12 12"><rect width="5" height="5" fill="#0293ce"/><rect x="7" width="5" height="5" fill="#0293ce"/><rect y="7" width="5" height="5" fill="#0293ce"/><rect x="7" y="7" width="5" height="5" fill="#0293ce"/></svg>
    <span>Videos</span><span>Coming soon</span><span>Focused innovation</span><span class="on">Industrial Design</span><span>Mechanical Engineering</span><span>Science &amp; technology</span>
  </div>
  <div class="tiles">
    <div class="tile" style="background:radial-gradient(ellipse 140px 90px at 45% 45%,#6f9fc9,transparent 70%),linear-gradient(135deg,#f6f8fa 0%,#dfe8f0 55%,#a9c1d8 100%)" role="img" aria-label="Tablet and devices on a bright desk"></div>
    <div class="tile" style="background:radial-gradient(ellipse 160px 110px at 50% 50%,rgba(255,255,255,.25),transparent 70%),linear-gradient(135deg,#4fb6dc 0%,#1a88b8 50%,#0b5f86 100%)" role="img" aria-label="Industrial design product in blue light"><span>INDUSTRIAL DESIGN</span></div>
    <div class="tile" style="background:radial-gradient(ellipse 110px 130px at 60% 40%,#e8b2a8,transparent 70%),linear-gradient(135deg,#f5efe8 0%,#e3cfc4 55%,#c98f98 100%)" role="img" aria-label="Child drawing at a table"></div>
    <div class="tile" style="background:radial-gradient(ellipse 130px 120px at 40% 50%,#f0d4bf,transparent 70%),linear-gradient(135deg,#e6edf3 0%,#c2d1de 55%,#8ea6bd 100%)" role="img" aria-label="Young student at a study desk"></div>
    <div class="tile" style="background:radial-gradient(ellipse 150px 100px at 50% 55%,#ffffff,transparent 70%),linear-gradient(135deg,#f3f4f5 0%,#d6dadf 55%,#9ea7b1 100%)" role="img" aria-label="Technical sketches on paper"></div>
    <div class="tile" style="background:radial-gradient(ellipse 120px 90px at 55% 60%,#e24e7a,transparent 70%),linear-gradient(135deg,#f4efe9 0%,#e2d2c3 55%,#bfa188 100%)" role="img" aria-label="Books and a desk lamp on a shelf"></div>
  </div>
  <span class="more">Show more</span>
</section>

<footer class="footer grid-bg">
  <div class="about">
    <h4>About</h4>
    <p>Kelvaris is a development company specialised in green energy and sustainable solutions for clients worldwide.</p>
    <div class="brand">
      <div class="brand-mark" style="width:28px;height:28px"></div>
      <div>
        <div class="brand-name">KELVARIS</div>
        <div class="brand-sub">SUSTAINABLE SOLUTIONS</div>
      </div>
    </div>
  </div>
  <div>
    <h4>Expertise</h4>
    <div class="tags">
      <span>Design</span><span>Engineering</span><span>Sourcing</span>
      <span>Testing</span><span class="on">Manufacturing</span><span>Consulting</span>
      <span>Technology</span><span>Products &amp; sales</span>
    </div>
  </div>
  <div>
    <h4>Quick links</h4>
    <ul class="links">
      <li>Home</li><li>Clients</li>
      <li>Work</li><li>About</li>
      <li>Expertise</li><li>News</li>
      <li>Approach</li><li>Contact</li>
    </ul>
  </div>
</footer>
<div class="copyright">Copyright © Kelvaris. All Rights Reserved.</div>

</body>
</html>
```